Need a business cards for a hair dressing salon.

Target Market(s)

Target woman for Hair cuts, bridal makeup, occasion, fashion makeup and etc.

Industry/Entity Type

Hair

Font styles to use
Serif
Script

Requirements
Must have
• - Business card to be memorable and recognizable

- Please include the following on the business card:
- Business name: Salon Marolin
- Name: Nilumi Jayasekara (Name Must be changeable)
- Occupation: Hair Dresser & Beautician
- Contact number: 04 731 6 CURL
- Email: mail@marolin.com.au
- Facebook (please use image): www.facebook.com/marolin.com.au
Nice to have
• Font Styles:
Business Name - Script
Other Text - Serif

```html
<!DOCTYPE html>
<html lang="en">
<head>
<meta charset="utf-8">
<title>Salon Marolin – Business Card</title>
<link rel="stylesheet" href="https://fonts.googleapis.com/css2?family=Great+Vibes&family=Tinos:wght@400&display=swap">
<style>
  :root {
    --backdrop: #9a9a9a;
    --card-white: #fbfbfb;
    --facet-light: #ffffff;
    --facet-shade: #e9e9ea;
    --crimson: #c8164c;
    --brand: #c12a6a;
  }
  * { box-sizing: border-box; margin: 0; padding: 0; }
  html, body {
    width: 1200px;
    height: 910px;
    overflow: hidden;
    background: var(--backdrop);
  }
  .canvas {
    width: 1200px;
    height: 910px;
    display: flex;
    align-items: center;
    justify-content: center;
  }
  .business-card {
    position: relative;
    width: 1050px;
    height: 600px;
    background: var(--card-white);
    box-shadow: 0 14px 30px rgba(0,0,0,0.25);
    overflow: hidden;
    font-family: "Tinos", "Times New Roman", serif;
    color: var(--crimson);
  }
  .card-texture {
    position: absolute;
    inset: 0;
    background:
      linear-gradient(125deg, var(--facet-light) 0%, var(--facet-shade) 38%, var(--facet-light) 60%, var(--facet-shade) 100%);
    opacity: 0.8;
  }
  .card-content {
    position: relative;
    height: 100%;
  }
  .brand-name {
    position: absolute;
    top: 110px;
    left: 0;
    right: 0;
    text-align: center;
    font-family: "Great Vibes", cursive;
    font-size: 124px;
    line-height: 1;
    color: var(--brand);
    font-weight: 400;
  }
  .person-name {
    position: absolute;
    top: 318px;
    left: 0;
    right: 0;
    text-align: center;
    font-size: 48px;
    font-weight: 400;
    letter-spacing: 0.5px;
  }
  .occupation {
    position: absolute;
    top: 384px;
    left: 0;
    right: 0;
    text-align: center;
    font-size: 21px;
    letter-spacing: 1.5px;
    text-transform: uppercase;
  }
  .contact-row {
    position: absolute;
    left: 70px;
    right: 70px;
    bottom: 62px;
    display: flex;
    justify-content: space-between;
    align-items: center;
    list-style: none;
  }
  .contact-item {
    display: flex;
    align-items: center;
    gap: 14px;
    font-size: 25px;
    letter-spacing: 0.5px;
  }
  .contact-icon {
    width: 24px;
    height: 24px;
    flex: none;
  }
</style>
</head>
<body>
<main class="canvas">
  <article class="business-card">
    <div class="card-texture" role="img" aria-label="Faint white low-poly geometric texture across the card"></div>
    <div class="card-content">
      <h1 class="brand-name">Salon Marolin</h1>
      <h2 class="person-name">Nilumi Jayasekara</h2>
      <p class="occupation">Hair Dresser &amp; Beautician</p>
      <ul class="contact-row">
        <li class="contact-item">
          <svg class="contact-icon" viewBox="0 0 24 24" aria-hidden="true">
            <path d="M6.6 3.5l2.6 3.6-1.7 2.2c1.2 2.6 3.3 4.7 5.9 5.9l2.2-1.7 3.6 2.6-1.5 3.3C11 19.2 4.8 13 4.5 6.2z" fill="none" stroke="var(--crimson)" stroke-width="1.8" stroke-linejoin="round"/>
          </svg>
          <span>04 731 6 CURL</span>
        </li>
        <li class="contact-item">
          <svg class="contact-icon" viewBox="0 0 24 24" aria-hidden="true">
            <circle cx="12" cy="12" r="4" fill="none" stroke="var(--crimson)" stroke-width="1.8"/>
            <path d="M16 8v5.5a2.5 2.5 0 0 0 5 0V12a9 9 0 1 0-3.5 7.1" fill="none" stroke="var(--crimson)" stroke-width="1.8" stroke-linecap="round"/>
          </svg>
          <span>mail@marolin.com.au</span>
        </li>
        <li class="contact-item">
          <svg class="contact-icon" viewBox="0 0 24 24" aria-hidden="true">
            <rect x="3" y="3" width="18" height="18" rx="2" fill="none" stroke="var(--crimson)" stroke-width="1.8"/>
          </svg>
          <span>/marolin.com.au</span>
        </li>
      </ul>
    </div>
  </article>
</main>
</body>
</html>
```